Business card design for a real estate company

We need a business card design a real estate development company called "Vantrelo Holding SA" in Switzerland. Space needed for two phone numbers in international format (one is +7 (912) xxx-xx-xx, the other +41 (76) xxx-xx-xx), e-mail (mb@vantrelo.example), name, position and address of the company:
Rue des Tilleuls 24
CH-1700 Fribourg
Switzerland

Target Market(s)

Potential partners, architects, banks etc..

Industry/Entity Type

Business

Requirements
Must have
• Slight, elegant.
Should not have
• Do not include illustrations of buildings etc..

```html
<!DOCTYPE html>
<html lang="en">
<head>
<meta charset="utf-8">
<title>Vantrelo Holding SA — Business Card</title>
<link rel="stylesheet" href="https://fonts.googleapis.com/css2?family=Arimo:wght@400;700&display=swap">
<style>
  :root {
    --page: #ffffff;
    --card-center: #4d382c;
    --card-edge: #2b1e17;
    --tan: #d8b89a;
    --white: #f4efe9;
    --rule: #a88c74;
  }
  * { margin: 0; padding: 0; box-sizing: border-box; }
  html, body {
    width: 1200px; height: 363px; overflow: hidden;
    background: var(--page);
    font-family: "Arimo", Arial, sans-serif;
  }
  .canvas { position: relative; width: 1200px; height: 363px; }
  .card {
    position: absolute; top: 0; height: 363px;
    background: radial-gradient(ellipse at 50% 45%, var(--card-center) 0%, var(--card-edge) 85%);
    color: var(--white);
  }
  .card--front { left: 0; width: 578px; }
  .card--back { left: 594px; width: 606px; }

  .wordmark {
    font-weight: 700; color: var(--tan);
    font-size: 21px; letter-spacing: 7px; white-space: nowrap;
  }
  .country {
    font-weight: 700; color: var(--white);
    font-size: 14px; letter-spacing: 3px; text-align: right;
  }

  .front-rule { position: absolute; top: 92px; width: 1px; height: 152px; background: var(--rule); }
  .front-rule--left { left: 68px; }
  .front-rule--right { left: 528px; }
  .front-brand { position: absolute; left: 80px; top: 152px; width: 436px; }
  .front-brand .country { margin-top: 8px; }

  .back-brand { position: absolute; right: 44px; top: 52px; text-align: right; }
  .back-brand .country { margin-top: 10px; }
  .back-rule { position: absolute; left: 0; right: 0; top: 140px; height: 1px; background: var(--rule); }

  .contact-person { position: absolute; left: 62px; top: 190px; }
  .person-name { font-weight: 700; font-size: 17px; letter-spacing: 2px; text-transform: uppercase; }
  .person-role { font-weight: 700; font-size: 13px; letter-spacing: 2px; color: var(--tan); margin-top: 10px; }

  .address { position: absolute; left: 334px; top: 180px; font-weight: 700; letter-spacing: 2px; }
  .address-label { font-size: 13px; color: var(--tan); text-transform: uppercase; }
  .address-line { font-size: 15px; margin-top: 7px; }

  .contact-row {
    position: absolute; left: 32px; right: 30px; top: 334px;
    display: flex; justify-content: space-between;
    font-size: 10px; font-weight: 700; letter-spacing: 2.5px; color: var(--tan);
    text-transform: uppercase;
  }
  .contact-row .value { text-transform: none; }
</style>
</head>
<body>
<div class="canvas">
  <section class="card card--front">
    <div class="front-rule front-rule--left"></div>
    <div class="front-rule front-rule--right"></div>
    <div class="front-brand">
      <div class="wordmark">Vantrelo Holding SA</div>
      <div class="country">Switzerland</div>
    </div>
  </section>

  <section class="card card--back">
    <div class="back-brand">
      <div class="wordmark">Vantrelo Holding SA</div>
      <div class="country">Switzerland</div>
    </div>
    <div class="back-rule"></div>

    <div class="contact-person">
      <div class="person-name">Marc Dubois</div>
      <div class="person-role">Director</div>
    </div>

    <div class="address">
      <div class="address-label">Address:</div>
      <div class="address-line">Rue des Tilleuls 24</div>
      <div class="address-line">CH-1700 Fribourg</div>
      <div class="address-line">Switzerland</div>
    </div>

    <div class="contact-row">
      <span>Phone: <span class="value">+7 (912) xxx-xx-xx</span></span>
      <span class="value">+41 (76) xxx-xx-xx</span>
      <span>Email: <span class="value">mb@vantrelo.example</span></span>
    </div>
  </section>
</div>
</body>
</html>
```